Coral Journey Mate - A Travel Services Website

Sunreef Home Rentals is a company that provides travels services to home owners and travellers to Barbados. Coral Journey Mate is a particular brand targeting travelling guests with specific set of travel services. The brand slogan is:

'Getting you the best for less'

The travel services will include:

- Coral Journey Mate Perks Pass
- Car Hire Quote Service
- Mobile Phone Sim Cards
- Prepaid Debit Cards
- Airport Hotel Booking
- Airport Lounge Booking
- Airport Parking

There will also be a travel planner function for guests.

The main puropse of the site is as follows:

1. Registration for the Coral Journey Mate Perks Pass

2. Creation of user account which the guest will frequently return to check for updates

3. Purchase of ancillary travel products and services

4. To use the Travel Planner

5. To gather data on holiday home owners in Barbados

A site map can be seen at the following link:

http://plotgridly.example/outlines/viewMap/4kqzvbn8ytrwpa2fuh5ximc07jldg6sqenoa9rvb33kf2pyq71

Webpage templates (2 required)

The first will be form control heavy (text boxes, checkboxes ect). It will need failure and success messages / indicators etc.

The second will be a general content area with a secondary navigation area (i.e for sub sections of the current section). This will house text / headings and images.

Both will require header, primary navigation, content and footer areas.

N.B. Please not that I am not technical and the above webtemplate narrative has been supplied by my web developer/programmer. If you have any questions, please ask me any questions and I will get an answer from him.

Target Market(s)

My customers tend to be:

Sex: Female
Age: 24-55
Location: UK, USA, Canada
Social Class: A,B,C1
Income: Medium income bracket

They are possibly visiting Barbados for the first and only time. It is an expensive destination and is accessible to people with a medium to high income. They still desire 'value for money'. Therefore the sight must give guests confidence that Coral Journey Mate is 'their friend', is seeking to offer the best value deals for their vacation/holiday.

Industry/Entity Type

Travel

Requirements
Must have
• The site templates must be professional, aspirational, trustworthy, reassuring, clean, innovative, fun. When people visit the site they should be excited about the savings that they can make and want to return as there is a perceived benefit for them. It must look expensive and professional in its projected image.
Nice to have
• Smooth currved lines, seperated boxed areas for content, as simple and uncluttered layout and it must be simple to read!
Should not have
• It should not be cartoonly, despite my attached logo and must not look cheap.

```html
<!DOCTYPE html>
<html lang="en">
<head>
<meta charset="utf-8">
<title>Coral Journey Mate – Car Hire</title>
<link href="https://fonts.googleapis.com/css2?family=Open+Sans:ital,wght@0,400;0,600;0,700;1,700&family=Arimo:wght@400;700&display=swap" rel="stylesheet">
<style>
:root{
  --page-top:#e9e9e9;
  --page-mid:#f7f7f7;
  --orange:#f6a90f;
  --orange-dark:#e39100;
  --hero-blue:#16a6d2;
  --hero-blue-dark:#0d8dbb;
  --heading-blue:#1a95c8;
  --text:#555555;
  --text-dark:#333333;
  --line:#e4e4e4;
  --button-grey:#7a7a7a;
  --login-red:#c8201c;
  --white:#ffffff;
  --flutter:#8fd3f0;
  --friend:#3b5a9a;
}
*{box-sizing:border-box;margin:0;padding:0}
html,body{width:1043px;height:1200px;overflow:hidden}
body{background:var(--page-mid);font-family:"Arimo",Arial,sans-serif;color:var(--text)}
.page{position:relative;width:1000px;height:1150px;transform:scale(1.043);transform-origin:0 0;
  background:linear-gradient(180deg,var(--page-top) 0,#f1f1f1 380px,var(--page-mid) 700px,#fafafa 1030px)}
.abs{position:absolute}

/* brand */
.brand{left:68px;top:24px;width:120px;height:120px;border-radius:50%;background:var(--orange);
  display:flex;align-items:center;justify-content:center;text-align:center;z-index:3;
  border:4px solid var(--white)}
.brand span{font-family:"Open Sans",sans-serif;font-weight:700;font-size:15px;line-height:17px;color:var(--white)}

/* login */
.login{top:43px;left:550px;display:flex;gap:7px;align-items:center}
.login .field{width:107px;height:24px;border:1px solid #cfcfcf;border-radius:5px;background:var(--white);
  font-size:12px;color:#666;padding:5px 7px;box-shadow:0 0 3px rgba(0,0,0,.12)}
.login .btn-login{width:48px;height:24px;border-radius:5px;background:var(--login-red);color:var(--white);
  font-size:12px;text-align:center;line-height:24px}
.login .links{font-size:11px;line-height:13px;color:#111;margin-left:-1px}

/* nav */
.main-nav{left:150px;top:77px;width:770px;height:37px;background:var(--orange);border-radius:0 8px 0 0;
  padding:0 10px 0 44px;display:flex;align-items:center;justify-content:space-between;
  font-family:"Open Sans",sans-serif;font-weight:600;font-size:11.6px;letter-spacing:-.1px;
  color:var(--white);text-shadow:0 1px 1px rgba(0,0,0,.25);white-space:nowrap;overflow:hidden}
.main-nav .sep{margin:0 2px}

/* hero */
.hero{left:86px;top:113px;width:834px;height:220px;border-radius:0 0 9px 9px;
  background:linear-gradient(180deg,var(--hero-blue) 0,var(--hero-blue-dark) 100%);color:var(--white)}
.hero h1{position:absolute;left:26px;top:50px;font-family:"Open Sans",sans-serif;font-style:italic;font-weight:700;
  font-size:32px;letter-spacing:-.5px}
.hero h2{position:absolute;left:29px;top:94px;font-family:"Open Sans",sans-serif;font-weight:600;font-size:14.5px}
.hero p{position:absolute;left:29px;top:115px;width:450px;font-size:12px;line-height:15px}
.hero .apply{position:absolute;left:30px;top:174px;width:97px;height:24px;border-radius:5px;
  background:linear-gradient(180deg,#ffc43c,var(--orange-dark));font-family:"Open Sans",sans-serif;
  font-weight:700;font-size:12.5px;text-align:center;line-height:24px;text-shadow:0 1px 1px rgba(0,0,0,.3)}
.hero .photo{position:absolute;left:500px;top:18px;width:285px;height:176px;border-radius:10px;
  background:radial-gradient(ellipse at 50% 45%,#f2f4f5 0,#c9d0d3 55%,rgba(22,166,210,0) 75%)}
.hero .pager{position:absolute;left:752px;top:192px;display:flex;gap:4px}
.hero .pager span{width:14px;height:14px;background:var(--white);color:var(--login-red);font-size:9px;
  text-align:center;line-height:14px;border-radius:2px}
.hero .pager .on{background:var(--orange);color:var(--white)}

/* panel */
.panel{left:87px;top:350px;width:831px;height:720px;background:#fafafa;border:1px solid #dcdcdc;border-radius:6px}
.panel-head{height:41px;background:var(--white);border-bottom:1px solid #e2e2e2;border-radius:6px 6px 0 0;
  box-shadow:0 2px 3px rgba(0,0,0,.06);position:relative}
.panel-head .icon{position:absolute;left:13px;top:5px}
.panel-head h3{position:absolute;left:45px;top:10px;font-size:16px;font-weight:700;color:var(--heading-blue)}
.panel-head .request{position:absolute;right:12px;top:11px;width:102px;height:21px;background:var(--button-grey);
  color:var(--white);font-size:12px;text-align:center;line-height:21px;border:1px solid #5f5f5f}

.section-title{position:absolute;font-size:14px;font-weight:700;color:var(--text)}
.section-title small{font-size:12px;font-weight:400;color:#444;margin-left:3px}

table.quotes{position:absolute;left:10px;width:808px;border-collapse:collapse;background:var(--white);
  border:1px solid #ececec;border-radius:5px;font-size:12px;color:var(--text)}
table.quotes th{height:27px;text-align:left;color:var(--heading-blue);font-size:12.5px;font-weight:700;
  padding-left:10px;border-bottom:1px solid var(--line)}
table.quotes td{height:29px;padding-left:9px;border-top:1px solid var(--line)}
table.quotes th,table.quotes td{border-right:1px solid var(--line)}
table.quotes th:last-child,table.quotes td:last-child{border-right:none}
table.quotes th.cur{padding-left:4px}
table.quotes .num{text-align:center;padding-left:0}
.act{display:inline-block;height:19px;background:var(--button-grey);color:var(--white);font-size:12px;
  line-height:19px;text-align:center;border:1px solid #5f5f5f;margin-right:1px}
.act.view{width:44px}
.act.cancel{width:53px}

/* footer */
.footer-band{left:0;top:1030px;width:1000px;height:120px;background:var(--orange)}
.copyright{left:89px;top:1087px;font-size:14px;color:var(--white)}
.social{top:1083px;height:22px;border-radius:3px;font-size:11.5px;font-weight:700;text-align:center;line-height:22px}
.social.flutter{left:752px;width:77px;background:var(--flutter);color:#1f6f92}
.social.friend{left:836px;width:81px;background:var(--friend);color:var(--white)}
</style>
</head>
<body>
<div class="page">

  <div class="abs footer-band"></div>

  <div class="abs brand"><span>Coral<br>Journey<br>Mate</span></div>

  <form class="abs login">
    <div class="field">username</div>
    <div class="field">password</div>
    <div class="btn-login">Login</div>
    <div class="links">Forgot Password?<br>Register New</div>
  </form>

  <nav class="abs main-nav">
    <span>Airport Parking</span><span class="sep">|</span>
    <span>Airport Hotel</span><span class="sep">|</span>
    <span>Airport Lounge</span><span class="sep">|</span>
    <span>Car Hire</span><span class="sep">|</span>
    <span>Attractions</span><span class="sep">|</span>
    <span>Travel Money</span><span class="sep">|</span>
    <span>Mobile Sim Cards</span><span class="sep">|</span>
    <span>Perks Pass</span>
  </nav>

  <section class="abs hero">
    <h1>Getting you the best for less</h1>
    <h2>Reserve a rental car and get a great rate online</h2>
    <p>Lorem ipsum dolor sit amet, consectetur adipiscing elit. Nullam metus nisi, sagittis semper cursus id, sollicitudin non justo. Mauris at elit sollicitudin diam vulputate ultrices dignissim quis velit. Quisque pretium lectus eget diam suscipit .</p>
    <div class="apply">Apply Now!</div>
    <div class="photo" role="img" aria-label="Photo of a silver four-wheel-drive rental car"></div>
    <div class="pager"><span>1</span><span class="on">2</span><span>3</span><span>4</span></div>
  </section>

  <main class="abs panel">
    <div class="panel-head">
      <svg class="icon" width="28" height="28" viewBox="0 0 28 28">
        <circle cx="14" cy="14" r="13" fill="#f6a90f" stroke="#fff" stroke-width="1.5"/>
        <rect x="8" y="10" width="12" height="8" rx="2" fill="#fff"/>
        <rect x="9.5" y="7.5" width="9" height="4" rx="1" fill="#fff"/>
        <circle cx="10.5" cy="15" r="1.2" fill="#f6a90f"/>
        <circle cx="17.5" cy="15" r="1.2" fill="#f6a90f"/>
        <rect x="9" y="18" width="2.5" height="2.5" fill="#fff"/>
        <rect x="16.5" y="18" width="2.5" height="2.5" fill="#fff"/>
      </svg>
      <h3>Car Hire</h3>
      <div class="request">Request Prices</div>
    </div>

    <div class="section-title" style="left:11px;top:63px">Open Quotes</div>
    <table class="quotes" style="top:84px">
      <colgroup><col style="width:135px"><col style="width:89px"><col style="width:130px"><col style="width:89px"><col style="width:95px"><col style="width:85px"><col style="width:67px"><col></colgroup>
      <tr><th>Pick Up Location</th><th>Date</th><th>Drop Off Location</th><th>Date</th><th>Driver’s Age</th><th>Car Group</th><th class="cur">Currency</th><th></th></tr>
      <tr><td>Some Airport</td><td>12/09.2010</td><td>At Home</td><td>12/09/2011</td><td class="num">35</td><td>Economy</td><td class="num">$</td><td><span class="act view">View</span><span class="act cancel">Cancel</span></td></tr>
      <tr><td>Some Airport</td><td>12/09.2010</td><td>At Home</td><td>12/09/2011</td><td class="num">31</td><td>Family</td><td class="num">£</td><td><span class="act view">View</span><span class="act cancel">Cancel</span></td></tr>
      <tr><td>Some Airport</td><td>12/09.2010</td><td>At Home</td><td>12/09/2011</td><td class="num">41</td><td>Economy</td><td class="num">$</td><td><span class="act view">View</span><span class="act cancel">Cancel</span></td></tr>
    </table>

    <div class="section-title" style="left:17px;top:225px">Accepted Quotes <small>(The hire provider still needs to confirm booking)</small></div>
    <table class="quotes" style="top:249px">
      <colgroup><col style="width:135px"><col style="width:89px"><col style="width:130px"><col style="width:89px"><col style="width:95px"><col style="width:85px"><col style="width:67px"><col></colgroup>
      <tr><th>Pick Up Location</th><th>Date</th><th>Drop Off Location</th><th>Date</th><th>Driver’s Age</th><th>Car Group</th><th class="cur">Currency</th><th></th></tr>
      <tr><td>Some Airport</td><td>12/09.2010</td><td>At Home</td><td>12/09/2011</td><td class="num">35</td><td>Economy</td><td class="num">$</td><td><span class="act view">View</span><span class="act cancel">Cancel</span></td></tr>
      <tr><td>Some Airport</td><td>12/09.2010</td><td>At Home</td><td>12/09/2011</td><td class="num">31</td><td>Family</td><td class="num">£</td><td><span class="act view">View</span><span class="act cancel">Cancel</span></td></tr>
      <tr><td>Some Airport</td><td>12/09.2010</td><td>At Home</td><td>12/09/2011</td><td class="num">41</td><td>Economy</td><td class="num">$</td><td><span class="act view">View</span><span class="act cancel">Cancel</span></td></tr>
    </table>

    <div class="section-title" style="left:17px;top:389px">Confirmed Bookings</div>
    <table class="quotes" style="top:413px">
      <colgroup><col style="width:135px"><col style="width:89px"><col style="width:130px"><col style="width:89px"><col style="width:95px"><col style="width:85px"><col style="width:67px"><col></colgroup>
      <tr><th>Pick Up Location</th><th>Date</th><th>Drop Off Location</th><th>Date</th><th>Driver’s Age</th><th>Car Group</th><th class="cur">Currency</th><th></th></tr>
      <tr><td>Some Airport</td><td>12/09.2010</td><td>At Home</td><td>12/09/2011</td><td class="num">35</td><td>Economy</td><td class="num">$</td><td><span class="act view">View</span></td></tr>
      <tr><td>Some Airport</td><td>12/09.2010</td><td>At Home</td><td>12/09/2011</td><td class="num">31</td><td>Family</td><td class="num">£</td><td><span class="act view">View</span></td></tr>
      <tr><td>Some Airport</td><td>12/09.2010</td><td>At Home</td><td>12/09/2011</td><td class="num">41</td><td>Economy</td><td class="num">$</td><td><span class="act view">View</span></td></tr>
      <tr><td>Some Airport</td><td>12/09.2010</td><td>At Home</td><td>12/09/2011</td><td class="num">41</td><td>Economy</td><td class="num">$</td><td><span class="act view">View</span></td></tr>
      <tr><td>Some Airport</td><td>12/09.2010</td><td>At Home</td><td>12/09/2011</td><td class="num">41</td><td>Economy</td><td class="num">$</td><td><span class="act view">View</span></td></tr>
      <tr><td>Some Airport</td><td>12/09.2010</td><td>At Home</td><td>12/09/2011</td><td class="num">41</td><td>Economy</td><td class="num">$</td><td><span class="act view">View</span></td></tr>
      <tr><td>Some Airport</td><td>12/09.2010</td><td>At Home</td><td>12/09/2011</td><td class="num">41</td><td>Economy</td><td class="num">$</td><td><span class="act view">View</span></td></tr>
      <tr><td>Some Airport</td><td>12/09.2010</td><td>At Home</td><td>12/09/2011</td><td class="num">41</td><td>Economy</td><td class="num">$</td><td><span class="act view">View</span></td></tr>
    </table>
  </main>

  <div class="abs copyright">Copyright © 2010 Coral Journey Mate. All rights reserved.</div>
  <div class="abs social flutter">Flutterly</div>
  <div class="abs social friend">Friendfold</div>

</div>
</body>
</html>
```